Business Card Design Project - Tall Maple

We are looking for a new business card design. Our company name is Tall Maple Communication Solutions. Our primary function is to provide our clients with communication solutions. These solutions include commercial phone systems and T1 and Fiber Internet lines. Another major part of the business is cabling new buildings with CAT5 cable for both data and phone.

Industry/Entity Type

Communication

Requirements
Must have
• The cards need to be two sided and have some bleeding edge color.
Nice to have
• We are going to upload our current logo BUT we are not married to this logo. If you want to incorporate a re-designed logo with the new business card - please feel free to do so. We are looking for a new bold look that is very colorful yet professional.

```html
<!DOCTYPE html>
<html lang="en">
<head>
<meta charset="utf-8">
<title>Tall Maple Communication Solutions — Business Cards</title>
<link rel="stylesheet" href="https://fonts.googleapis.com/css2?family=Questrial&family=Roboto:wght@400;700&display=swap">
<style>
  :root {
    --navy: #0b2d5c;
    --navy-soft: #3d5a85;
    --bright-blue: #1c66b3;
    --paper: #ffffff;
    --backdrop: #dcdde0;
    --ink: #1d1d1f;
  }
  * { box-sizing: border-box; margin: 0; padding: 0; }
  html, body {
    width: 1200px; height: 900px; overflow: hidden;
    background: var(--backdrop);
  }
  .stage { position: relative; width: 1200px; height: 900px; }
  .card {
    position: absolute;
    width: 520px; height: 320px;
    border-radius: 18px;
    overflow: hidden;
    box-shadow: 0 4px 14px rgba(0,0,0,0.18);
  }

  /* Company name: one font, one weight, one colour */
  .company-name {
    position: absolute;
    font-family: "Questrial", sans-serif;
    font-weight: 400;
    line-height: 1.15;
  }

  /* Front */
  .card--front { left: 50px; top: 290px; background: var(--navy); }
  .front-orb {
    position: absolute; left: 380px; top: 40px;
    width: 260px; height: 260px; border-radius: 50%;
    background: var(--navy-soft); opacity: 0.75;
  }
  .card--front .company-name {
    left: 48px; top: 122px; font-size: 28px; color: var(--paper);
  }

  /* Back */
  .card--back { left: 630px; top: 290px; background: var(--paper); }
  .back-orb {
    position: absolute; left: -110px; top: 20px;
    width: 250px; height: 250px; border-radius: 50%;
    background: var(--navy);
  }
  .card--back .company-name {
    left: 236px; top: 24px; font-size: 20px; color: var(--navy);
  }
  .name-band {
    position: absolute; left: 196px; right: 0; top: 115px; height: 40px;
    background: linear-gradient(90deg, var(--navy) 0%, var(--navy) 40%, var(--bright-blue) 100%);
    color: var(--paper);
    font-family: "Roboto", sans-serif; font-weight: 700; font-size: 20px;
    letter-spacing: 0.5px; text-transform: uppercase;
    display: flex; align-items: center; padding-left: 24px;
  }
  .contact {
    position: absolute; left: 196px; top: 176px;
    font-family: "Roboto", sans-serif; font-size: 14px; line-height: 19px;
    color: var(--ink); list-style: none;
  }
  .contact li { display: flex; align-items: center; gap: 5px; }
  .contact svg { width: 12px; height: 12px; fill: var(--navy); flex: none; }
</style>
</head>
<body>
<main class="stage">
  <section class="card card--front" aria-label="Card front">
    <div class="front-orb"></div>
    <p class="company-name">Tall Maple<br>Communication Solutions</p>
  </section>

  <section class="card card--back" aria-label="Card back">
    <div class="back-orb"></div>
    <p class="company-name">Tall Maple<br>Communication Solutions</p>
    <div class="name-band">Dana Whitfield</div>
    <ul class="contact">
      <li>1480 W Ridgeview Avenue, Suite 300</li>
      <li>Tempe, AZ 85281</li>
      <li>
        <svg viewBox="0 0 12 12" aria-label="Phone"><path d="M1 4c0-2 2-3 5-3s5 1 5 3l-2 1-1-1.5H4L3 5zM3 6h6l1 5H2z"/></svg>
        480.555.0142 or 800.555.0199 (24/7)
      </li>
      <li>
        <svg viewBox="0 0 12 12" aria-label="Fax"><path d="M3 1h5v3H3zM1 5h10v5H1zM3 7h2v1H3zM7 7h2v1H7z"/></svg>
        800.555.0173
      </li>
      <li>
        <svg viewBox="0 0 12 12" aria-label="Mobile"><path d="M3 0h6v12H3zM4 1.5v7h4v-7z"/></svg>
        480.555.0186
      </li>
    </ul>
  </section>
</main>
</body>
</html>
```